Natural Skincare Product Labels Design

We are looking for a designer to create elegant but quirky, functional product labels for our natural skincare range.
The labels must reflect our brand’s values of simplicity, luxury, and the natural, handmade essence of our products.
https://www.instagram.com/tolvarenskincare
1. Key Details
Packaging Dimensions
Container Types: Transparent jars.
Sizes for Body Products:
Diameter: 64mm–68mm.
Heights: 80mm, 88mm, and 97mm (lid height: 15mm).
Sizes for Face Creams:
Diameter: 60mm.
Height: 50mm (lid height: 15mm).
Label Fit: For body products, ideally one label size to fit all jar sizes.
For the smaller face cream jars, a separate, tailored label is required.
2. Label Placement
Options include a wrapped-around label or a combination of wrapped-around and top-of-jar elements.
Transparent jars mean the label must leave space for the product to be visible (e.g., partial wrap or cutout areas).
3. Content Requirements
Product Name: Prominently displayed.
Ingredient List: Dedicated space required.
Disclaimer/Usage Instructions: Include space for this information.
4. Design Goals
Look & Feel: Simple, upmarket, and natural, with a handmade essence.
Logo Usage: Our logo is finalized and available in gold, black, and white variants. Use Josefin Bold font for the logo if adjustments are required.
Color Palette: Neutral tones (e.g., whites, blacks, golds) are preferred, with flexibility for subtle pops of color tied to each product’s main ingredient.
5. Imagery
Open to including images and colours (e.g., botanical illustrations) that highlight the main ingredient (e.g., coffee beans, turmeric root, or honeycomb). Also open to labels having a prominent colour to tie it in to the main ingredient.
Alternatively, no images can also work for a clean design.
6. Current Design Context
Our temporary design features gold leaf on top and a simple handmade side label. We’re seeking to elevate this to a more polished, cohesive design.
7. Product Line
- Body Products (Larger Jars)
Mivo Body Butter
Key Ingredients: Guarana & Cupuaçu butter (inspired by Brazil).
Note: “Mivo” is slang for “bum.”
Manuka Honey Body Butter
Key Ingredients: Manuka honey (from New Zealand) & Cupuaçu butter.
Coffee Body Scrub
Key Ingredients: Coffee and Demerara sugar.
Whipped Body Soap - Turmeric
Key Ingredients: Turmeric and Bentonite clay.
Whipped Body Soap - Banana
- Face Products (Smaller Jars)
Face Cream
Key Ingredients: Carrot Oil and Raspberry Oil.
Features natural UV protection.
Good Night Cream
Key Ingredients: Enriched with Magnesium.
Promotes relaxation and restful sleep.
8. Submission Guidelines
Flexibility: Design should allow for consistent branding across all products while accommodating the varying jar sizes and ingredient focus.
Material Considerations: Labels should complement the transparent jars and allow the product inside to remain partially visible.
Print Elements: Incorporating gold accents is a plus but should not overpower the design.
We’re excited to see your vision for a label that celebrates the natural beauty and high quality of our skincare range. Please include mockups to showcase the design in use, particularly on transparent jars of varying sizes.
women 20-50 years of age

```html
<!DOCTYPE html>
<html lang="en">
<head>
<meta charset="UTF-8">
<title>Tolvaren — Manuka Honey Body Butter Label</title>
<link href="https://fonts.googleapis.com/css2?family=IBM+Plex+Sans:ital,wght@0,400;0,700;1,400&family=Fraunces:opsz,wght@9..144,700&display=swap" rel="stylesheet">
<style>
  :root {
    --backdrop: #333333;
    --label: #ffffff;
    --copper: #ad5f2b;
    --gold: #c0913a;
    --ink: #222222;
    --spec: #ffffff;
  }
  * { margin: 0; padding: 0; box-sizing: border-box; }
  html, body {
    width: 1200px; height: 1200px; overflow: hidden;
    background: var(--backdrop);
    font-family: "IBM Plex Sans", sans-serif;
  }
  .spec {
    position: absolute; left: 71px; top: 74px;
    color: var(--spec); font-size: 25px; line-height: 32px;
  }
  .label {
    position: absolute; left: 59px; top: 282px;
    width: 1081px; height: 635px;
    background: var(--label); border-radius: 28px;
  }
  .brand {
    position: absolute; left: 64px; top: 108px;
    display: flex; align-items: center; gap: 12px;
    color: var(--gold); font-weight: 700; font-size: 26px;
    letter-spacing: 0.12em; text-transform: uppercase;
  }
  .brand-dot {
    width: 14px; height: 14px; border-radius: 50%;
    border: 2px solid var(--gold);
  }
  .key-ingredients {
    position: absolute; left: 63px; top: 255px;
    color: var(--copper); font-size: 25px;
  }
  .product-name {
    position: absolute; left: 62px; top: 295px;
    color: var(--copper);
    font-family: "Fraunces", serif; font-weight: 700;
    font-size: 58px; line-height: 64px; letter-spacing: -0.01em;
  }
  .rule-h {
    position: absolute; left: 64px; top: 508px;
    width: 636px; height: 1px; background: var(--copper);
  }
  .rule-v {
    position: absolute; left: 700px; top: 63px;
    width: 1px; height: 509px; background: var(--copper);
  }
  .tagline {
    position: absolute; left: 62px; top: 527px;
    font-style: italic; font-size: 22px; color: var(--ink);
  }
  .volume {
    position: absolute; right: 395px; top: 529px;
    font-size: 22px; color: var(--ink);
  }
  .info {
    position: absolute; left: 733px; width: 300px;
    font-size: 21.5px; line-height: 27px; color: var(--ink);
  }
  .info h2 {
    color: var(--copper); font-size: 21px; font-weight: 700;
    line-height: 27px;
  }
  .info-ingredients { top: 129px; }
  .info-usage { top: 371px; }
  .dots {
    position: absolute; left: 733px; top: 328px;
    display: flex; gap: 9px;
  }
  .dots span {
    width: 5px; height: 5px; border-radius: 50%; background: var(--copper);
  }
</style>
</head>
<body>
  <div class="spec">Label Size<br>85 x 50 mm</div>

  <section class="label">
    <div class="brand"><span class="brand-dot"></span>Tolvaren</div>

    <p class="key-ingredients">Manuka honey • Cupuaçu butter</p>
    <h1 class="product-name">Manuka Honey<br>Body Butter</h1>

    <div class="rule-h"></div>
    <div class="rule-v"></div>

    <p class="tagline">Crafted by Hand, Inspired by Nature</p>
    <p class="volume">125 ml</p>

    <div class="info info-ingredients">
      <h2>Ingredients</h2>
      <p>Manuka honey, Cupuaçu butter, Shea butter, Sunflower oil, Vitamin E, Beeswax, Lavender essential oil.</p>
    </div>

    <div class="dots"><span></span><span></span><span></span></div>

    <div class="info info-usage">
      <h2>How to Use</h2>
      <p>After a bath or shower, massage your dry skin to absorb the nourishing goodness.</p>
    </div>
  </section>
</body>
</html>
```